The Long Lantern of a Harbour Town: A Chronicle of Patience, Courage and Kinship

I require designs for the front cover, rear cover and spine for a printed book. The book is the personal account of a stroke survivor.

Dimensions requested by publisher:|

Front + rear covers = 130 x 195mm with 3-5mm bleed
Spine = c. 10mm

Target Market(s)

Worldwide

Font styles to use
Decorative
Script

Requirements
Must have
• The text for the back cover (and I have attached photos for the accompanying headshot):

"Mira Ostend had become a successful commercial lawyer in Tanzania with a professional career that spanned almost two decades. One week after celebrating her law firm’s 5th anniversary her life changed dramatically when at 4am one morning she suffered an ischaemic stroke.

After losing the use of the right side of her body and her ability to speak and swallow, Mira was forced to undergo a full system reboot. In this brutally honest account of her life before and after the stroke Mira describes her physical and mental battles, how she managed to accept the condition and deal with the accompanying feelings of shame.

Her story is one of rebirth, hope and ultimately transformation, offering practical advice for stroke survivors, their families and anyone embarking on a rehabilitation programme following serious illness."
Nice to have
• Modern but elegant feel. Something that signifies the metamorphosis of a butterfly, or transformation in general.

```html
<!DOCTYPE html>
<html lang="en">
<head>
<meta charset="utf-8">
<title>The Long Lantern of a Harbour Town – Cover Presentation</title>
<link href="https://fonts.googleapis.com/css2?family=Yesteryear&family=Open+Sans:wght@600;700&family=Encode+Sans+Condensed:wght@400&display=swap" rel="stylesheet">
<style>
  :root {
    --paper: #ffffff;
    --cream-top: #f4ef9f;
    --cream-bottom: #fbf9e2;
    --red: #e8130f;
    --ink: #111111;
    --wing-red: #d8150f;
    --suit: #c85bbd;
    --photo-bg: #b7a7a3;
  }
  * { box-sizing: border-box; margin: 0; padding: 0; }
  html, body { width: 1200px; height: 900px; overflow: hidden; background: var(--paper); }
  .board { position: relative; width: 1200px; height: 900px; font-family: "Open Sans", sans-serif; color: var(--ink); }

  .label { position: absolute; font-family: "Open Sans", sans-serif; font-weight: 600; letter-spacing: 1px; text-align: center; }
  .label--actual { left: 60px; width: 639px; top: 662px; font-size: 18px; letter-spacing: 1.5px; }
  .label--front { left: 750px; width: 409px; top: 92px; font-size: 18px; }

  .wrap { position: absolute; left: 60px; top: 175px; width: 639px; height: 461px; }

  /* back cover */
  .back { position: absolute; left: 0; top: 0; width: 308px; height: 461px;
    background: linear-gradient(to bottom, var(--cream-top), var(--cream-bottom)); }
  .back__title { position: absolute; top: 34px; left: 0; width: 100%; text-align: center;
    font-family: "Yesteryear", cursive; font-size: 21px; white-space: nowrap; }
  .back__subtitle { position: absolute; top: 72px; left: 0; width: 100%; text-align: center;
    font-weight: 600; font-size: 11px; letter-spacing: 0.3px; }
  .back__blurb { position: absolute; top: 104px; left: 6px; width: 296px; text-align: center;
    font-family: "Encode Sans Condensed", sans-serif; font-size: 6.1px; line-height: 15px; }
  .back__blurb p + p { margin-top: 15px; }
  .back__photo { position: absolute; left: 22px; top: 282px; width: 148px; height: 128px;
    background: linear-gradient(135deg, #c9c3b8, var(--photo-bg) 55%, #a56fa7); }
  .back__author { position: absolute; left: 190px; top: 278px; font-weight: 700; font-size: 14px; letter-spacing: 0.5px; }

  /* spine */
  .spine { position: absolute; left: 308px; top: 0; width: 22px; height: 461px; background: var(--red); color: #fff;
    display: flex; justify-content: center; }
  .spine__text { writing-mode: vertical-rl; white-space: nowrap; padding-top: 10px; display: flex; align-items: center; gap: 10px; }
  .spine__author { font-weight: 700; font-size: 8px; letter-spacing: 1px; }
  .spine__title { font-family: "Yesteryear", cursive; font-size: 14px; }
  .spine__subtitle { font-weight: 600; font-size: 6.5px; }

  /* front cover (scalable) */
  .front { position: absolute; width: calc(var(--u) * 409); height: calc(var(--u) * 611);
    background: linear-gradient(to bottom, var(--cream-top), var(--cream-bottom) 60%, var(--cream-top)); overflow: hidden; }
  .front--wrap { --u: 0.755px; left: 330px; top: 0; }
  .front--solo { --u: 1px; left: 750px; top: 122px; outline: 2px solid var(--ink); }

  .front__flourish { position: absolute; width: calc(var(--u) * 150); height: calc(var(--u) * 170);
    background: radial-gradient(ellipse at var(--corner), rgba(232,19,15,0.55), rgba(232,19,15,0.18) 55%, rgba(232,19,15,0) 75%); }
  .front__flourish--tl { left: 0; top: 0; --corner: 0% 0%; }
  .front__flourish--tr { right: 0; top: 0; --corner: 100% 0%; }
  .front__flourish--bl { left: 0; bottom: 0; --corner: 0% 100%; }
  .front__flourish--br { right: 0; bottom: 0; --corner: 100% 100%; }

  .front__title { position: absolute; left: 0; width: 100%; top: calc(var(--u) * 18); text-align: center;
    font-family: "Yesteryear", cursive; line-height: 1; }
  .front__title span { display: block; }
  .front__title .t1 { font-size: calc(var(--u) * 50); }
  .front__title .t2 { font-size: calc(var(--u) * 56); margin-top: calc(var(--u) * 6); }
  .front__title .t3 { font-size: calc(var(--u) * 50); margin-top: calc(var(--u) * 2); }
  .front__subtitle { position: absolute; left: 0; width: 100%; top: calc(var(--u) * 186); text-align: center;
    font-weight: 600; font-size: calc(var(--u) * 20); line-height: 1.25; letter-spacing: calc(var(--u) * 0.8); }
  .front__art { position: absolute; left: calc(var(--u) * 34); top: calc(var(--u) * 251);
    width: calc(var(--u) * 341); height: calc(var(--u) * 298);
    background: radial-gradient(ellipse at 50% 45%, var(--suit) 0 14%, var(--wing-red) 15% 55%, rgba(216,21,15,0) 72%); }
  .front__author { position: absolute; left: 0; width: 100%; top: calc(var(--u) * 568); text-align: center;
    font-weight: 700; font-size: calc(var(--u) * 23); letter-spacing: calc(var(--u) * 1.5); }
</style>
</head>
<body>
<main class="board">

  <section class="wrap" aria-label="Full cover wrap">
    <article class="back">
      <h2 class="back__title">The Long Lantern of a Harbour Town</h2>
      <p class="back__subtitle">A Chronicle of Patience, Courage and Kinship</p>
      <div class="back__blurb">
        <p>Mira Ostend had become a successful commercial lawyer in Tanzania with a professional career that spanned almost<br>two decades. One week after celebrating her law firm’s 5th anniversary her life changed dramatically<br>when at 4am one morning she suffered an ischaemic stroke</p>
        <p>After losing the use of the right side of her body and her ability to speak and swallow, Mira was forced to undergo a full system reboot<br>In this brutally honest account of her life before and after the stroke Mira describes her physical and mental battles<br>how she managed to accept the condition and deal with the accompanying feelings of shame</p>
        <p>Her story is one of rebirth, hope and ultimately transformation, offering practical advice for stroke survivors, their families<br>and anyone embarking on a rehabilitation programme following serious illness</p>
      </div>
      <div class="back__photo" role="img" aria-label="Headshot of the author in a lilac blazer"></div>
      <p class="back__author">Mira Ostend</p>
    </article>

    <aside class="spine">
      <div class="spine__text">
        <span class="spine__author">Mira Ostend</span>
        <span class="spine__title">The Long Lantern of a Harbour Town</span>
        <span class="spine__subtitle">A Chronicle of Patience, Courage and Kinship</span>
      </div>
    </aside>

    <article class="front front--wrap">
      <div class="front__flourish front__flourish--tl" role="img" aria-label="Red decorative corner flourish"></div>
      <div class="front__flourish front__flourish--tr" role="img" aria-label="Red decorative corner flourish"></div>
      <div class="front__flourish front__flourish--bl" role="img" aria-label="Red decorative corner flourish"></div>
      <div class="front__flourish front__flourish--br" role="img" aria-label="Red decorative corner flourish"></div>
      <h1 class="front__title"><span class="t1">The</span><span class="t2">Long Lantern</span><span class="t3">of a Harbour Town</span></h1>
      <p class="front__subtitle">A Chronicle of Patience, Courage<br>and Kinship</p>
      <div class="front__art" role="img" aria-label="Illustration of a woman in a purple suit with large red butterfly wings"></div>
      <p class="front__author">Mira Ostend</p>
    </article>
  </section>
  <p class="label label--actual">ACTUAL SIZE</p>

  <p class="label label--front">Front Cover</p>
  <article class="front front--solo">
    <div class="front__flourish front__flourish--tl" role="img" aria-label="Red decorative corner flourish"></div>
    <div class="front__flourish front__flourish--tr" role="img" aria-label="Red decorative corner flourish"></div>
    <div class="front__flourish front__flourish--bl" role="img" aria-label="Red decorative corner flourish"></div>
    <div class="front__flourish front__flourish--br" role="img" aria-label="Red decorative corner flourish"></div>
    <h2 class="front__title"><span class="t1">The</span><span class="t2">Long Lantern</span><span class="t3">of a Harbour Town</span></h2>
    <p class="front__subtitle">A Chronicle of Patience, Courage<br>and Kinship</p>
    <div class="front__art" role="img" aria-label="Illustration of a woman in a purple suit with large red butterfly wings"></div>
    <p class="front__author">Mira Ostend</p>
  </article>

</main>
</body>
</html>
```